Flyer for Harbourline Accounting & Taxation, a local tax practice

Flyer for my business to be distributed locally in the Western Suburb of Melbourne (Size: DL, Fold: Flat, Backside: Blank) This will include below information (Font, color and capitalization of the text is for the designer's creativity):
Harbourline Accounting & Taxation Your Local Tax Accountant
ABN: 37 481 259 604
Address: 9 Marlo Place, Wattle Bend
kolvend@hbatx.com.au
Call Tobias on 0419 786 205 to book your appointment
Services we offer:
Individual & Company Tax Returns
Company & Trust formation
Business Advisory
Bookkeeping
BAS & IAS
Payroll
TPAR
Please include the logo of the business attached which was designed by PixelForum few years ago.
Please include the NBF, RCQ and Lumo logos somewhere in the bottom, preferable the same size and aligned (attached)

```html
<!DOCTYPE html>
<html lang="en">
<head>
<meta charset="utf-8">
<title>Harbourline Accounting &amp; Taxation – Flyer</title>
<link rel="stylesheet" href="https://fonts.googleapis.com/css2?family=Montserrat:wght@500&family=Oswald:wght@300;400;700&display=swap">
<style>
  :root {
    --page-bg: #aec4d0;
    --flyer-top: #474747;
    --flyer-bottom: #000000;
    --orange: #ff5a10;
    --orange-band: #ff6a1a;
    --white: #ffffff;
    --badge-bg: #ffffff;
  }
  * { margin: 0; padding: 0; box-sizing: border-box; }
  html, body {
    width: 707px; height: 1200px; overflow: hidden;
    background: var(--page-bg);
  }
  .flyer {
    position: absolute; left: 85px; top: 30px;
    width: 536px; height: 1140px; overflow: hidden;
    background: radial-gradient(ellipse 120% 55% at 5% 0%, var(--flyer-top) 0%, #1a1a1a 55%, var(--flyer-bottom) 80%);
    font-family: "Oswald", "Arial Narrow", sans-serif;
    color: var(--white);
  }
  .flyer > * { position: absolute; white-space: nowrap; line-height: 1; transform-origin: left top; }

  .illustration--calculator {
    left: 388px; top: 219px; width: 132px; height: 146px;
    background: linear-gradient(160deg, #3a6fe0 0%, #2a55c4 55%, #f08a2a 100%);
    border-radius: 10px; transform: rotate(10deg); transform-origin: center;
  }
  .illustration--savings {
    left: 333px; top: 612px; width: 203px; height: 318px;
    background: linear-gradient(180deg, #f5b81c 0%, #e79a10 30%, #2b3560 50%, #1c2444 100%);
    border-radius: 18px 18px 10px 10px;
  }

  .brand-mark { left: 54px; top: 50px; width: 70px; height: 70px; background: var(--orange); }
  .brand-name {
    left: 140px; font-family: "Montserrat", sans-serif; font-weight: 500;
    color: var(--orange);
  }
  .brand-name--main { top: 62px; font-size: 34px; letter-spacing: 1px; }
  .brand-name--sub { top: 103px; font-size: 21px; }

  .headline { left: 42px; font-size: 69px; font-weight: 700; letter-spacing: -1px; transform: scaleX(0.85); }
  .headline--1 { top: 162px; }
  .headline--2 { top: 224px; }

  .services-title { left: 46px; top: 325px; font-size: 48px; font-weight: 700; color: var(--orange); letter-spacing: -0.5px; transform: scaleX(0.86); }

  .service { font-size: 31px; font-weight: 400; letter-spacing: -0.3px; transform: scaleX(0.85); }
  .chevron { width: 12px; height: 20px; }
  .service--1 { left: 92px; top: 390px; }
  .service--2 { left: 92px; top: 447px; }
  .service--3 { left: 92px; top: 504px; }
  .service--4 { left: 92px; top: 561px; }
  .service--5 { left: 92px; top: 618px; }
  .service--6 { left: 350px; top: 509px; }
  .service--7 { left: 350px; top: 566px; }
  .chevron--1 { left: 49px; top: 397px; }
  .chevron--2 { left: 49px; top: 454px; }
  .chevron--3 { left: 49px; top: 511px; }
  .chevron--4 { left: 49px; top: 568px; }
  .chevron--5 { left: 49px; top: 625px; }
  .chevron--6 { left: 317px; top: 516px; }
  .chevron--7 { left: 317px; top: 573px; }

  .booking { left: 46px; font-size: 44px; font-weight: 300; transform: scaleX(0.94); }
  .booking--1 { top: 699px; }
  .booking--2 { top: 746px; }

  .call-band { left: 0; top: 811px; width: 351px; height: 110px; background: var(--orange-band); }
  .call-name { left: 46px; top: 824px; font-size: 37px; font-weight: 700; transform: scaleX(0.88); }
  .call-icon { left: 48px; top: 871px; width: 26px; height: 26px; }
  .call-number { left: 96px; top: 864px; font-size: 39px; font-weight: 700; transform: scaleX(0.88); }

  .abn { left: 48px; top: 944px; font-size: 35px; font-weight: 700; transform: scaleX(0.8); }
  .abn-label { color: var(--orange); margin-right: 16px; }

  .contact { font-size: 21px; font-weight: 300; }
  .contact-address--1 { left: 79px; top: 1018px; }
  .contact-address--2 { left: 81px; top: 1040px; }
  .contact-email { left: 83px; top: 1073px; }
  .icon-pin { left: 52px; top: 1021px; width: 14px; height: 18px; }
  .icon-mail { left: 51px; top: 1077px; width: 16px; height: 12px; }

  .badge { background: var(--badge-bg); }
  .badge--body { left: 303px; top: 992px; width: 99px; height: 51px; }
  .badge--software { left: 303px; top: 1048px; width: 99px; height: 55px; }
  .badge--registration { left: 408px; top: 992px; width: 89px; height: 111px; }
</style>
</head>
<body>
<main class="flyer">
  <div class="illustration illustration--calculator" role="img" aria-label="3D calculator illustration with orange keys and a percent coin"></div>
  <div class="illustration illustration--savings" role="img" aria-label="3D illustration of gold dollar coins dropping into a navy safe"></div>

  <div class="brand-mark" aria-hidden="true"></div>
  <div class="brand-name brand-name--main">HARBOURLINE</div>
  <div class="brand-name brand-name--sub">Accounting &amp; Taxation</div>

  <h1 class="headline headline--1">YOUR LOCAL TAX</h1>
  <div class="headline headline--2">ACCOUNTANT</div>

  <h2 class="services-title">SERVICES WE OFFER</h2>

  <svg class="chevron chevron--1" viewBox="0 0 12 20" aria-hidden="true"><polyline points="2,2 10,10 2,18" fill="none" stroke="#ff5a10" stroke-width="3"/></svg>
  <div class="service service--1">Individual &amp; Company Tax Returns</div>
  <svg class="chevron chevron--2" viewBox="0 0 12 20" aria-hidden="true"><polyline points="2,2 10,10 2,18" fill="none" stroke="#ff5a10" stroke-width="3"/></svg>
  <div class="service service--2">Company &amp; Trust formation</div>
  <svg class="chevron chevron--3" viewBox="0 0 12 20" aria-hidden="true"><polyline points="2,2 10,10 2,18" fill="none" stroke="#ff5a10" stroke-width="3"/></svg>
  <div class="service service--3">Business Advisory</div>
  <svg class="chevron chevron--4" viewBox="0 0 12 20" aria-hidden="true"><polyline points="2,2 10,10 2,18" fill="none" stroke="#ff5a10" stroke-width="3"/></svg>
  <div class="service service--4">Bookkeeping</div>
  <svg class="chevron chevron--5" viewBox="0 0 12 20" aria-hidden="true"><polyline points="2,2 10,10 2,18" fill="none" stroke="#ff5a10" stroke-width="3"/></svg>
  <div class="service service--5">BAS &amp; IAS</div>
  <svg class="chevron chevron--6" viewBox="0 0 12 20" aria-hidden="true"><polyline points="2,2 10,10 2,18" fill="none" stroke="#ff5a10" stroke-width="3"/></svg>
  <div class="service service--6">Payroll</div>
  <svg class="chevron chevron--7" viewBox="0 0 12 20" aria-hidden="true"><polyline points="2,2 10,10 2,18" fill="none" stroke="#ff5a10" stroke-width="3"/></svg>
  <div class="service service--7">TPAR</div>

  <div class="booking booking--1">TO BOOK YOUR</div>
  <div class="booking booking--2">APPOINTMENT</div>

  <div class="call-band" aria-hidden="true"></div>
  <div class="call-name">CALL TOBIAS</div>
  <svg class="call-icon" viewBox="0 0 24 24" aria-hidden="true"><path fill="#ffffff" d="M6.6 10.8c1.4 2.8 3.8 5.1 6.6 6.6l2.2-2.2c.3-.3.7-.4 1-.2 1.1.4 2.3.6 3.6.6.6 0 1 .4 1 1V20c0 .6-.4 1-1 1C10.6 21 3 13.4 3 4c0-.6.4-1 1-1h3.5c.6 0 1 .4 1 1 0 1.3.2 2.5.6 3.6.1.3 0 .7-.2 1l-2.3 2.2z"/></svg>
  <div class="call-number">0419 786 205</div>

  <div class="abn"><span class="abn-label">ABN</span>37 481 259 604</div>

  <svg class="icon-pin" viewBox="0 0 14 18" aria-hidden="true"><path fill="#ff5a10" d="M7 0a7 7 0 0 0-7 7c0 5 7 11 7 11s7-6 7-11a7 7 0 0 0-7-7zm0 9.5A2.5 2.5 0 1 1 7 4.5a2.5 2.5 0 0 1 0 5z"/></svg>
  <div class="contact contact-address--1">9 Marlo Place,</div>
  <div class="contact contact-address--2">Wattle Bend</div>
  <svg class="icon-mail" viewBox="0 0 16 12" aria-hidden="true"><rect width="16" height="12" rx="1" fill="#ff5a10"/><polyline points="1,1 8,7 15,1" fill="none" stroke="#000" stroke-width="1.3"/></svg>
  <div class="contact contact-email">kolvend@hbatx.com.au</div>

  <div class="badge badge--body" role="img" aria-label="Professional body membership badge"></div>
  <div class="badge badge--software" role="img" aria-label="Accounting software partner badge"></div>
  <div class="badge badge--registration" role="img" aria-label="Registered tax agent badge"></div>
</main>
</body>
</html>
```